Website Design - Financial Services Software

We are looking for website designs for our public website.
Some competitor sites we like are
www.ledgerwick.com.au
www.pluvo.com.au
www.plannerbeam.com
www.quorvia.com.au

A wireframe example of our site can be found at
http://tmw4rp.draftpane.com/

Attached is our logo.

Industry/Entity Type

Financial

```html
<!DOCTYPE html>
<html lang="en">
<head>
<meta charset="utf-8">
<title>Verantis — Smarter Financial Strategies</title>
<link rel="stylesheet" href="https://fonts.googleapis.com/css2?family=Cinzel:wght@400;600&family=Open+Sans:wght@300;400;600&family=Tinos&display=swap">
<style>
:root{
  --blue:#1a72c9;
  --blue-dark:#1462b0;
  --nav-active:#1560ad;
  --brown:#6e3409;
  --brown-light:#8e4a12;
  --tan:#ab9a7e;
  --tile-active:#62a2e0;
  --ink:#1f1f1f;
  --footer:#2d2d2d;
  --footer-bottom:#111;
  --white:#fff;
}
*{margin:0;padding:0;box-sizing:border-box}
html,body{width:1135px;height:1200px;overflow:hidden;background:var(--white)}
body{position:relative;font-family:"Open Sans",sans-serif;color:var(--ink)}
.abs{position:absolute}

/* header */
.brand{left:188px;top:16px;width:110px;text-align:center}
.brand-mark{width:44px;height:44px;margin:0 auto 6px;background:#111;border-radius:50%}
.brand-name{font-family:"Cinzel",serif;font-weight:600;font-size:19px;color:#111;letter-spacing:.5px;line-height:1}
.brand-tag{font-family:"Cinzel",serif;font-size:5.5px;color:#111;letter-spacing:.3px;margin-top:2px}
.social{top:46px;width:29px;height:29px;border-radius:2px}
.btn-head{top:46px;height:29px;width:88px;color:var(--white);font-family:"Cinzel",serif;font-size:12.5px;display:flex;align-items:center;justify-content:center;border-radius:2px}
.btn-login{left:768px;background:var(--brown)}
.btn-signup{left:859px;background:var(--blue-dark)}

/* nav */
.nav{left:0;top:114px;width:1135px;height:33px;background:var(--blue)}
.nav ul{position:absolute;left:188px;top:0;display:flex;list-style:none;height:33px}
.nav li{height:33px;display:flex;align-items:center;justify-content:center;color:var(--white);font-family:"Cinzel",serif;font-size:13.5px;border-right:1px solid rgba(0,0,0,.12)}
.nav li.active{background:var(--nav-active)}

/* hero */
.hero{left:0;top:147px;width:1135px;height:418px;background:linear-gradient(100deg,#5c5a58 0%,#3f3b37 35%,#4a4540 60%,#2f2d2c 100%)}
.video{left:188px;top:235px;width:342px;height:214px;background:var(--white);padding:5px}
.video-still{width:100%;height:100%;background:linear-gradient(90deg,#6b5442,#8a7361 50%,#9b8e80)}
.video svg{position:absolute;left:146px;top:72px}
.hero-title{left:559px;top:230px;font-family:"Cinzel",serif;font-size:25px;color:var(--white);letter-spacing:.5px;white-space:nowrap}
.hero-sub{left:560px;top:270px;width:400px;font-weight:300;font-size:17px;line-height:21px;color:var(--white)}
.thumb{top:331px;width:148px;height:117px;background:#d6d6d6}
.thumb-img{height:90px}
.thumb-cap{height:27px;display:flex;align-items:center;justify-content:center;font-size:12px;color:#333;background:#cfcfcf}

/* features */
.features{left:0;top:565px;width:1135px;height:352px;background:linear-gradient(90deg,#e3e2e0,#e8eaee 50%,#dfe4ec)}
.features h2{position:absolute;left:0;width:1135px;top:30px;text-align:center;font-family:"Tinos",serif;font-weight:400;font-size:31px;color:var(--blue)}
.features p{position:absolute;text-align:center;font-size:10.6px;line-height:15.5px;color:#222}
.tile{top:769px;width:121px;height:82px;border-radius:3px;background:var(--tan);color:#2a2a2a;font-weight:600;font-size:12.5px;line-height:12.5px;text-align:center;display:flex;flex-direction:column;align-items:center;justify-content:center;gap:6px}
.tile.active{background:var(--tile-active);color:var(--white)}

/* cta */
.cta{left:0;top:917px;width:1135px;height:92px;background:var(--blue)}
.cta-text{left:188px;top:955px;width:450px;font-family:"Cinzel",serif;font-size:14.2px;color:var(--white);white-space:nowrap}
.cta-btn{left:655px;top:945px;width:292px;height:38px;border-radius:3px;background:linear-gradient(var(--brown-light),var(--brown));color:var(--white);font-family:"Cinzel",serif;font-size:17px;display:flex;align-items:center;justify-content:center}

/* footer */
.footer{left:0;top:1009px;width:1135px;height:158px;background:var(--footer)}
.footer-logo{left:189px;top:1048px;width:110px;height:88px;background:#000;display:flex;flex-direction:column;align-items:center;justify-content:center;gap:5px}
.footer-logo .brand-mark{width:30px;height:30px;background:#eee;margin:0}
.footer-logo .brand-name{color:#eee;font-size:13px}
.fcol{top:1052px;color:#ddd}
.fcol h3{font-family:"Tinos",serif;font-weight:400;font-size:15px;color:#eee;padding-bottom:6px;border-bottom:1px solid #444;margin-bottom:10px}
.fcol li{list-style:none;font-size:11px;line-height:19px;display:flex;align-items:center;gap:5px;white-space:nowrap}
.fcol .sq{width:10px;height:10px;background:#eee;display:inline-block;flex:none}
.copyright{left:0;top:1167px;width:1135px;height:33px;background:var(--footer-bottom)}
.copyright span{position:absolute;left:188px;top:10px;font-size:9.5px;color:#ccc}
</style>
</head>
<body>

<header>
  <div class="abs brand">
    <div class="brand-mark"></div>
    <div class="brand-name">VERANTIS</div>
    <div class="brand-tag">SMARTER FINANCIAL STRATEGIES</div>
  </div>
  <span class="abs social" style="left:616px;background:#3b5b98"></span>
  <span class="abs social" style="left:654px;background:#1da1e2"></span>
  <span class="abs social" style="left:692px;background:#7cc0e8"></span>
  <span class="abs social" style="left:730px;background:#f58a2b"></span>
  <a class="abs btn-head btn-login">Log in</a>
  <a class="abs btn-head btn-signup">Sign up</a>
</header>

<nav class="abs nav">
  <ul>
    <li class="active" style="width:93px">HOME</li>
    <li style="width:118px">FEATURES</li>
    <li style="width:81px">FAQ</li>
    <li style="width:115px">ABOUT US</li>
    <li style="width:115px">EXAMPLES</li>
    <li style="width:139px">CONTACT US</li>
    <li style="width:98px">BLOG</li>
  </ul>
</nav>

<section class="abs hero" role="img" aria-label="Background photo of financial advisers in a meeting"></section>
<div class="abs video">
  <div class="video-still" role="img" aria-label="Video still of an adviser in an office meeting"></div>
  <svg width="64" height="64" viewBox="0 0 64 64" aria-hidden="true">
    <circle cx="32" cy="32" r="29" fill="none" stroke="#fff" stroke-width="3"/>
    <path d="M25 19 L46 32 L25 45 Z" fill="#fff"/>
  </svg>
</div>
<h1 class="abs hero-title" style="font-weight:400">Smarter Financial Strategies</h1>
<p class="abs hero-sub">Values and Cash-flow focused fiancial software for financial planners</p>
<div class="abs thumb" style="left:562px">
  <div class="thumb-img" role="img" aria-label="Photo of hands reviewing documents with a pen" style="background:linear-gradient(#c6b3a3,#e5e2dd)"></div>
  <div class="thumb-cap">For planing Practices</div>
</div>
<div class="abs thumb" style="left:737px">
  <div class="thumb-img" role="img" aria-label="Photo of a business team group" style="background:linear-gradient(#8a8f9a,#3a2e2c)"></div>
  <div class="thumb-cap">For Dealer Groups</div>
</div>

<section class="abs features">
  <h2>Features</h2>
  <p style="top:82px;left:193px;width:749px">Lorem Ipsum is simply dummy text of the printing and typesetting industry. Lorem Ipsum has been the industry's standard dummy text ever since the 1500s, when an unknown printer took a galley of type and scrambled it to make a type specimen book.</p>
  <p style="top:128px;left:184px;width:767px">It has survived not only five centuries, but also the leap into electro- nic typesetting, remaining essentially unchanged. It was popularised in the 1960s with the release of Letraset sheets containing Lorem Ipsum passages,</p>
</section>

<div class="abs tile active" style="left:188px">
  <svg width="14" height="14" viewBox="0 0 14 14"><circle cx="8" cy="6" r="4.5" fill="none" stroke="#fff" stroke-width="1.8"/><path d="M5 9 L1 13" stroke="#fff" stroke-width="2"/></svg>
  Fact Find</div>
<div class="abs tile" style="left:315px">
  <svg width="14" height="14" viewBox="0 0 14 14"><rect x="2" y="1" width="9" height="12" fill="none" stroke="#2a2a2a" stroke-width="1.5"/><circle cx="10" cy="10" r="3" fill="#2a2a2a"/></svg>
  Online data</div>
<div class="abs tile" style="left:442px">
  <svg width="16" height="14" viewBox="0 0 16 14"><path d="M1 13 H15 M3 11 V7 L8 9 L13 2" stroke="#2a2a2a" stroke-width="2" fill="none"/></svg>
  Custom<br>Branding</div>
<div class="abs tile" style="left:570px">
  <svg width="16" height="14" viewBox="0 0 16 14"><rect x="5" y="0" width="6" height="4" fill="#2a2a2a"/><rect x="0" y="10" width="6" height="4" fill="#2a2a2a"/><rect x="10" y="10" width="6" height="4" fill="#2a2a2a"/><path d="M8 4 V7 M3 10 V7 H13 V10" stroke="#2a2a2a" stroke-width="1.3" fill="none"/></svg>
  Site<br>Intigration</div>
<div class="abs tile" style="left:697px">
  <svg width="14" height="14" viewBox="0 0 14 14"><path d="M7 1 L2 6 H5 V10 H9 V6 H12 Z M1 12 H13 V14 H1 Z" fill="#2a2a2a"/></svg>
  Upload File</div>
<div class="abs tile" style="left:826px">
  <svg width="14" height="14" viewBox="0 0 14 14"><circle cx="7" cy="4" r="3.5" fill="#2a2a2a"/><path d="M1 14 Q1 8 7 8 Q13 8 13 14 Z" fill="#2a2a2a"/></svg>
  User<br>Management</div>

<section class="abs cta"></section>
<p class="abs cta-text">Create an account today and begin your 30 day trial!</p>
<a class="abs cta-btn">Sign up Now!</a>

<footer class="abs footer"></footer>
<div class="abs footer-logo">
  <div class="brand-mark"></div>
  <div class="brand-name">VERANTIS</div>
</div>
<div class="abs fcol" style="left:346px;width:90px">
  <h3>About us</h3>
  <ul><li>About us</li><li>Support</li></ul>
</div>
<div class="abs fcol" style="left:499px;width:133px">
  <h3>Getting Started</h3>
  <ul><li>Why Verantis</li><li>Download a Summary</li><li>Verantis Videos</li></ul>
</div>
<div class="abs fcol" style="left:687px;width:103px">
  <h3>Legal</h3>
  <ul><li>Terms of Use</li><li>Privacy</li></ul>
</div>
<div class="abs fcol" style="left:826px;width:121px">
  <h3>Connect</h3>
  <ul><li><span class="sq"></span>Verantis on Linkora</li><li><span class="sq"></span>Verantis on Chirpline</li></ul>
</div>
<div class="abs copyright"><span>Copyright © 2014 Verantis Pty Ltd. All rights reserved.</span></div>

</body>
</html>
```